I need a design with just the number 24. must be in blue color (royal blue) should be large enough for people see must be in the center of page. Place a nice border around the page.

• Number 24 in Royal blue color

```html
<!DOCTYPE html>
<html lang="en">
<head>
<meta charset="UTF-8">
<title>Number 24</title>
<link href="https://fonts.googleapis.com/css2?family=Saira+Condensed:wght@800&display=swap" rel="stylesheet">
<style>
  :root {
    --royal-blue: #0222b3;
    --ornament-tint: rgba(2, 34, 179, 0.35);
    --paper: #ffffff;
  }
  html, body {
    margin: 0;
    padding: 0;
    overflow: hidden;
    background: var(--paper);
  }
  .canvas {
    position: relative;
    width: 1200px;
    height: 1000px;
    background: var(--paper);
    overflow: hidden;
  }
  .page-border {
    position: absolute;
    inset: 0;
    width: 1200px;
    height: 1000px;
  }
  .house-number {
    position: absolute;
    left: 308px;
    top: 49px;
    width: 584px;
    height: 900px;
    display: flex;
    align-items: center;
    justify-content: center;
    margin: 0;
    padding-left: 24px;
    box-sizing: border-box;
    font-family: "Saira Condensed", "Arial Narrow", sans-serif;
    font-weight: 800;
    font-size: 492px;
    line-height: 1;
    letter-spacing: 4px;
    color: var(--royal-blue);
  }
</style>
</head>
<body>
  <main class="canvas">
    <svg class="page-border" viewBox="0 0 1200 1000" aria-hidden="false">
      <g fill="none" stroke="var(--royal-blue)" stroke-width="3">
        <!-- outer frame -->
        <rect x="307.5" y="49.5" width="585" height="900"/>
        <!-- secondary vertical rules -->
        <line x1="320" y1="49.5" x2="320" y2="949.5"/>
        <line x1="878" y1="49.5" x2="878" y2="949.5"/>
        <!-- inner frame sides -->
        <line x1="326.5" y1="55.5" x2="326.5" y2="943.5"/>
        <line x1="871.5" y1="55.5" x2="871.5" y2="943.5"/>
        <!-- inner frame top, broken at the centre flourish -->
        <line x1="326.5" y1="55.5" x2="545" y2="55.5"/>
        <line x1="655" y1="55.5" x2="871.5" y2="55.5"/>
        <!-- inner frame bottom, broken at the centre flourish -->
        <line x1="326.5" y1="943.5" x2="545" y2="943.5"/>
        <line x1="655" y1="943.5" x2="871.5" y2="943.5"/>
      </g>
      <rect class="flourish flourish--top" x="555" y="50" width="90" height="70" rx="6"
            fill="var(--ornament-tint)" role="img" aria-label="Decorative scroll flourish at top centre of the frame"/>
      <rect class="flourish flourish--bottom" x="555" y="879" width="90" height="70" rx="6"
            fill="var(--ornament-tint)" role="img" aria-label="Decorative scroll flourish at bottom centre of the frame"/>
    </svg>
    <h1 class="house-number">24</h1>
  </main>
</body>
</html>
```